Bright Orchard
Bright & Fun-filled
Talia Brennick
Certified Holistic Wellness Coach, NLP Practitioner
no address pls
talia@brightorchard.com
www.brightorchard.com
To love oneself is the beginning of a lifelong romance. --Edwin Tarrow

```html
<!DOCTYPE html>
<html lang="en">
<head>
<meta charset="utf-8">
<title>Bright Orchard – Business Card</title>
<link href="https://fonts.googleapis.com/css2?family=Arimo:wght@400;700&display=swap" rel="stylesheet">
<style>
  :root {
    --stage: #e9eaec;
    --card-white: #ffffff;
    --card-shade: #e4e4e6;
    --brand-pink: #ee1f60;
    --ink-dark: #4a4a4c;
    --ink-mid: #6d6d70;
    --strip-text: #ffe3ec;
  }
  * { margin: 0; padding: 0; box-sizing: border-box; }
  html, body { width: 1200px; height: 830px; overflow: hidden; }
  body {
    background: var(--stage);
    font-family: "Arimo", Arial, sans-serif;
    position: relative;
  }
  .card {
    position: absolute;
    border-radius: 14px;
    overflow: hidden;
    box-shadow: 0 4px 14px rgba(0,0,0,0.18);
  }
  .card-front {
    left: 400px; top: 190px; width: 400px; height: 276px;
    background: linear-gradient(180deg, var(--card-white) 0%, var(--card-white) 55%, var(--card-shade) 100%);
  }
  .brand-line {
    position: absolute; left: 34px; top: 42px;
    display: flex; align-items: center; gap: 10px;
  }
  .brand-name {
    font-size: 36px; font-weight: 400; color: var(--ink-dark);
    letter-spacing: -0.5px;
  }
  .brand-dot {
    width: 20px; height: 20px; border-radius: 50%;
    background: var(--brand-pink);
  }
  .person { position: absolute; left: 36px; top: 118px; }
  .person-name {
    font-size: 17px; font-weight: 700; color: var(--brand-pink);
  }
  .person-title {
    margin-top: 4px; font-size: 10.5px; line-height: 1.35; color: var(--ink-mid);
  }
  .contact {
    position: absolute; left: 36px; top: 196px;
    font-size: 10.5px; line-height: 1.45; color: var(--ink-mid);
  }
  .web-strip {
    position: absolute; left: 0; right: 0; bottom: 0; height: 24px;
    background: var(--brand-pink);
    display: flex; align-items: center; justify-content: center;
    font-size: 10px; letter-spacing: 2.5px; color: var(--strip-text);
  }
  .card-back {
    top: 490px; width: 372px; height: 250px;
    display: flex; align-items: center; justify-content: center;
  }
  .card-back--pink { left: 210px; background: var(--brand-pink); }
  .card-back--white {
    left: 618px;
    background: linear-gradient(180deg, var(--card-white) 0%, var(--card-white) 60%, var(--card-shade) 100%);
  }
  .back-mark {
    display: flex; align-items: center; gap: 12px;
  }
  .back-mark .brand-name { font-size: 30px; }
  .card-back--pink .brand-name { color: var(--card-white); }
  .card-back--pink .brand-dot { background: var(--card-white); }
  .card-back--white .brand-name { color: var(--brand-pink); }
</style>
</head>
<body>
  <section class="card card-front" aria-label="Business card front">
    <div class="brand-line">
      <span class="brand-name">Bright Orchard</span>
      <span class="brand-dot"></span>
    </div>
    <div class="person">
      <p class="person-name">Talia Brennick</p>
      <p class="person-title">Certified Holistic Wellness Coach,<br>NLP Practitioner</p>
    </div>
    <div class="contact">
      <p>Phone: 555.014.2290</p>
      <p>Email: talia@brightorchard.com</p>
    </div>
    <div class="web-strip">www.brightorchard.com</div>
  </section>

  <section class="card card-back card-back--pink" aria-label="Business card back, pink">
    <div class="back-mark">
      <span class="brand-dot"></span>
      <span class="brand-name">Bright Orchard</span>
    </div>
  </section>

  <section class="card card-back card-back--white" aria-label="Business card back, white">
    <div class="back-mark">
      <span class="brand-dot"></span>
      <span class="brand-name">Bright Orchard</span>
    </div>
  </section>
</body>
</html>
```